KV Group

We need a new website for our company and since we had a very good work done for our logo in this site, we're back for the entire job.

Our company name is Marlowe Capital Group. We're adding files of examples of what we have done today. In my opinion we need a more attention lock in the site but yet financial simple work.

Our files (attached) will let you know what we have so far. We need a complete change but the colours should be the same, however you can change them not running away to far from the original, and of course matching with the logo.

We need examples for 3 kind of layouts.

- A HOME welcome layout
- An internal Layout with sidebar
- And internal Layout wide

We can buy image licenses if needed for assets.
Actually there are 5 slide images placed on the Welcome HOME, we need those there, but you can improve with better images to match the new website!!!

Target Market(s)

Clients looking for financial advisers, tax and funds specialist, currency advisers

Industry/Entity Type

Financial

Requirements
Must have
• all the fonts must be in accordance with the financial market sites........the welcome home page must be precise, neat and information accurate........the menu should be elegant........main focus on the Home page, should be also the PRIVATE ACCESS box log in.......

```html
<!DOCTYPE html>
<html lang="en">
<head>
<meta charset="utf-8">
<title>Marlowe Capital Group – History</title>
<link href="https://fonts.googleapis.com/css2?family=PT+Sans+Narrow:wght@400;700&family=Arimo:wght@400;700&display=swap" rel="stylesheet">
<style>
:root{
  --orange:#f07a1a;
  --orange-dark:#d9650b;
  --ink:#1d1d1d;
  --text:#3a3a3a;
  --muted:#555;
  --head-bg:#dfe5ee;
  --nav-bg:#1b1b1b;
  --footer-bg:#161616;
  --footer-link:#bdbdbd;
  --field:#ece8e2;
  --up:#1a9a2a;
  --down:#d21f1f;
}
*{box-sizing:border-box;margin:0;padding:0}
html,body{width:840px;height:1200px;overflow:hidden;background:#fff}
body{position:relative;font-family:"Arimo",Arial,sans-serif;color:var(--text)}
.narrow{font-family:"PT Sans Narrow",Arial,sans-serif}
.abs{position:absolute}

/* header */
.site-header{position:absolute;left:0;top:0;width:840px;height:98px;background:var(--head-bg)}
.brand{position:absolute;left:60px;top:20px;display:flex;align-items:center;gap:8px}
.brand-mark{width:26px;height:26px;background:var(--orange)}
.brand-name{font-family:"PT Sans Narrow",sans-serif;font-size:17px;color:#333;font-weight:700;letter-spacing:.5px}
.top-links{position:absolute;right:64px;top:58px;display:flex;align-items:center;gap:8px;font-family:"PT Sans Narrow",sans-serif;font-size:15px;color:#444}
.top-links svg{vertical-align:-3px;margin-right:4px}

/* nav */
.main-nav{position:absolute;left:0;top:98px;width:840px;height:52px;background:var(--nav-bg)}
.main-nav ul{list-style:none;display:flex;position:absolute;left:58px;top:0;height:52px}
.main-nav li{height:52px;line-height:52px;font-family:"PT Sans Narrow",sans-serif;font-size:15px;color:#fff;text-align:center;position:relative}
.main-nav li+li::before{content:"";position:absolute;left:0;top:22px;width:1px;height:8px;background:#555}
.main-nav li.active{background:var(--orange);height:56px}

/* hero */
.hero{position:absolute;left:58px;top:156px;width:532px;height:218px;background:linear-gradient(120deg,#c9d6e6 0%,#7f94b3 45%,#2d3a55 80%,#dfe6ef 100%)}
.hero-caption{position:absolute;left:-8px;top:100px;width:484px;height:78px;background:rgba(20,20,20,.82);padding:8px 18px}
.hero-caption h2{font-family:"PT Sans Narrow",sans-serif;font-weight:400;font-size:19px;color:var(--orange)}
.hero-caption p{font-family:"PT Sans Narrow",sans-serif;font-size:13.5px;color:#fff;line-height:1.35;margin-top:2px}
.dots{position:absolute;left:544px;top:382px;display:flex;gap:3px}
.dots span{width:8px;height:8px;border-radius:50%;border:1px solid #888;background:#fff}
.dots span.on{background:var(--orange);border-color:var(--orange-dark)}

/* private access */
.private-access{position:absolute;left:596px;top:156px;width:180px;height:218px;background:linear-gradient(180deg,var(--orange) 0%,#f59a4c 100%);padding:12px 8px}
.private-access h3{font-family:"PT Sans Narrow",sans-serif;font-weight:400;font-size:20px;color:#fff}
.pa-badge{position:absolute;right:12px;top:8px;width:34px;height:34px;border-radius:50%;background:#f5a35a;border:2px solid #fbd0a6}
.pa-field{position:absolute;left:8px;width:164px;height:22px;background:var(--field);font-size:9px;color:#888;padding:6px 7px}
.pa-forget{position:absolute;left:8px;top:118px;font-family:"PT Sans Narrow",sans-serif;font-size:11px;color:#fff}
.pa-login{position:absolute;left:8px;top:156px;width:74px;height:22px;background:#1b1b1b;color:#fff;font-size:10px;text-align:center;line-height:22px}
.pa-art{position:absolute;left:96px;top:108px;width:76px;height:96px;background:radial-gradient(circle at 50% 50%,#c9611f 0%,rgba(201,97,31,0) 70%)}

/* content */
.section-title{font-family:"PT Sans Narrow",sans-serif;font-weight:400;font-size:17px;color:var(--orange)}
.breadcrumb{position:absolute;left:460px;top:410px;width:114px;text-align:right;font-family:"PT Sans Narrow",sans-serif;font-size:11px;color:#333}
.intro{position:absolute;left:58px;top:434px;width:516px;font-family:"PT Sans Narrow",sans-serif;font-size:14px;line-height:1.3;color:#444}
.body-copy{font-size:8.6px;line-height:1.38;text-align:justify;color:var(--text);letter-spacing:.15px}
.body-copy p+p{margin-top:9px}
.photo{position:absolute;border:1px solid #ccc;box-shadow:0 1px 3px rgba(0,0,0,.35)}

/* sidebar */
.side-menu{position:absolute;left:596px;top:437px;width:180px;list-style:none}
.side-menu li{height:27px;line-height:26px;padding-left:28px;font-family:"PT Sans Narrow",sans-serif;font-size:15px;color:#444;position:relative;background:linear-gradient(90deg,#f1f1f1,rgba(255,255,255,0))}
.side-menu li::before{content:"›";position:absolute;left:12px;top:-1px;color:#555}
.side-menu li.active{background:var(--orange);color:#fff}
.side-menu li.active::before{color:#fff}

/* partners */
.partners{position:absolute;left:58px;top:834px;width:718px;height:42px;background:linear-gradient(180deg,#fff,#f1f1f1);border-top:1px solid #e5e5e5;border-bottom:1px solid #e0e0e0}
.partner{position:absolute;top:8px;height:26px;background:#cfcfcf}
.partner.round{width:26px;border-radius:50%;background:#3a3a3a}
.ticker{position:absolute;left:58px;top:896px;width:718px;height:22px;border:1px solid #e3e3e3;font-size:9px;font-weight:700;line-height:20px;white-space:nowrap;overflow:hidden;color:#222;padding-left:14px}
.ticker span{margin-right:20px}
.ticker .up{color:var(--up)}
.ticker .down{color:var(--down)}
.ticker .flat{color:var(--orange)}

/* footer */
.site-footer{position:absolute;left:0;top:938px;width:840px;height:262px;background:var(--footer-bg)}
.footer-col{position:absolute;top:18px}
.footer-col h4{font-family:"PT Sans Narrow",sans-serif;font-weight:400;font-size:16px;color:#fff;margin-bottom:4px}
.footer-col ul{list-style:none}
.footer-col li{font-family:"PT Sans Narrow",sans-serif;font-size:11px;color:var(--footer-link);line-height:18.4px}
.verified{position:absolute;left:634px;top:132px;width:106px;height:70px;background:#f3f3f3;border-radius:4px}
.copyright{position:absolute;left:0;top:210px;width:840px;text-align:center;font-family:"PT Sans Narrow",sans-serif;font-size:10px;color:#fff}
</style>
</head>
<body>

<header class="site-header">
  <div class="brand"><span class="brand-mark"></span><span class="brand-name">MARLOWE CAPITAL GROUP</span></div>
  <div class="top-links">
    <span><svg width="16" height="14" viewBox="0 0 16 14"><rect x="1" y="2" width="10" height="11" fill="none" stroke="#444" stroke-width="1.4"/><path d="M4 6h5M4 9h4M9 10l6-8" stroke="#444" stroke-width="1.4"/></svg>Apply Now</span>
    <span style="color:#888">|</span>
    <span><svg width="16" height="14" viewBox="0 0 16 14"><path d="M1 5q7-6 14 0l-2 2-2-1V4H5v2L3 7z" fill="#444"/><rect x="4" y="8" width="8" height="5" fill="#444"/></svg>Contact Us</span>
  </div>
</header>

<nav class="main-nav">
  <ul>
    <li style="width:92px">Home</li>
    <li class="active" style="width:62px">About us</li>
    <li style="width:108px">Investments</li>
    <li style="width:88px">Funds</li>
    <li style="width:108px">Brokerage</li>
    <li style="width:88px">Exchange</li>
    <li style="width:90px">Accounts</li>
  </ul>
</nav>

<section class="hero" role="img" aria-label="Photo of private bankers working together at a desk">
  <div class="hero-caption">
    <h2>Teamwork for your benefit</h2>
    <p>Our dedicated Private Bankers, will proactively keep you up to date with relevant information and provide a financial overview that enables you to make better decisions.</p>
  </div>
</section>
<div class="dots"><span class="on"></span><span></span><span></span><span></span><span></span></div>

<aside class="private-access">
  <h3>Private Access</h3>
  <div class="pa-badge"></div>
  <div class="pa-art" role="img" aria-label="Puzzle pieces illustration"></div>
  <div class="pa-field" style="top:58px">Acc. Number</div>
  <div class="pa-field" style="top:86px">Acc. password</div>
  <div class="pa-forget">Forget Password?</div>
  <div class="pa-login">LOGIN</div>
</aside>

<h2 class="section-title abs" style="left:58px;top:402px">History</h2>
<div class="breadcrumb">Home : About Us : History</div>
<p class="intro">Our dedicated Private Bankers, will proactively keep you up to date with relevant information and provide a financial overview that enables you to make better decisions.</p>

<div class="photo" style="left:58px;top:478px;width:156px;height:76px;background:linear-gradient(180deg,#6c7a93,#3b3f4a 60%,#c98d4a)" role="img" aria-label="City skyline at dusk"></div>
<div class="body-copy abs" style="left:226px;top:478px;width:348px">
  <p>Lorem ipsum dolor sit amet, consectetur adipisicing elit, sed do eiusmod tempor incididunt ut labore et dolore magna aliqua. Ut enim ad minim veniam, quis nostrud exercitation ullamco laboris nisi ut aliquip ex ea commodo consequat.</p>
  <p>Lorem ipsum dolor sit amet, consectetur adipisicing elit, sed do eiusmod tempor incididunt ut labore et dolore magna aliqua. Ut enim ad minim veniam,</p>
</div>
<div class="body-copy abs" style="left:58px;top:560px;width:516px">
  <p>quis nostrud exercitation ullamco laboris nisi ut aliquip ex ea commodo consequat.Lorem ipsum dolor sit amet, consectetur adipisicing elit, sed do eiusmod tempor incididunt ut labore et dolore magna aliqua. Ut enim ad minim veniam, quis nostrud exercitation ullamco laboris nisi ut aliquip ex ea commodo consequat.</p>
</div>

<h2 class="section-title abs" style="left:58px;top:613px">Our Mission</h2>
<div class="photo" style="left:58px;top:641px;width:156px;height:77px;background:linear-gradient(120deg,#8a8f94,#cfc7bc 50%,#5b5550)" role="img" aria-label="Business people meeting in an office"></div>
<div class="body-copy abs" style="left:226px;top:641px;width:348px">
  <p>Lorem ipsum dolor sit amet, consectetur adipisicing elit, sed do eiusmod tempor incididunt ut labore et dolore magna aliqua. Ut enim ad minim veniam, quis nostrud exercitation ullamco laboris nisi ut aliquip ex ea commodo consequat.</p>
  <p>Lorem ipsum dolor sit amet, consectetur adipisicing elit, sed do eiusmod tempor incididunt ut labore et dolore magna aliqua. Ut enim ad minim veniam,</p>
</div>
<div class="body-copy abs" style="left:58px;top:723px;width:516px">
  <p>quis nostrud exercitation ullamco laboris nisi ut aliquip ex ea commodo consequat.Lorem ipsum dolor sit amet, consectetur adipisicing elit, sed do eiusmod tempor incididunt ut labore et dolore magna aliqua. Ut enim ad minim veniam, quis nostrud exercitation ullamco laboris nisi ut aliquip ex ea commodo consequat.</p>
  <p>Lorem ipsum dolor sit amet, consectetur adipisicing elit, sed do eiusmod tempor incididunt ut labore et dolore magna aliqua. Ut enim ad minim veniam, quis nostrud exercitation ullamco laboris nisi ut aliquip ex ea commodo consequat.</p>
</div>

<h2 class="section-title abs" style="left:603px;top:402px">ABOUT US</h2>
<ul class="side-menu">
  <li class="active">History</li>
  <li>Expertize</li>
  <li>Identity</li>
  <li>Strategy</li>
</ul>
<div class="photo" style="left:602px;top:620px;width:166px;height:94px;background:linear-gradient(135deg,#2f7fd1,#7fbdf0 55%,#1d5aa8)" role="img" aria-label="Stock market figures on a blue screen"></div>
<div class="body-copy abs" style="left:603px;top:724px;width:166px">
  <p>Lorem ipsum dolor sit amet, consectetur adipisicing elit, sed do eiusmod tempor incididunt ut labore et dolore magna aliqua. Ut enim ad minim veniam, quis nostrud exercitation ullamco laboris nisi ut aliquip ex ea commodo consequat.</p>
</div>

<h2 class="abs narrow" style="left:58px;top:810px;font-size:15px;font-weight:400;color:#111">Our Partners</h2>
<div class="partners">
  <svg class="abs" style="left:-2px;top:14px" width="8" height="12" viewBox="0 0 8 12"><path d="M6 1 1 6l5 5" fill="none" stroke="#222" stroke-width="2"/></svg>
  <div class="partner" style="left:14px;width:52px;background:#b7c2d8"></div>
  <div class="partner round" style="left:80px;background:#e6e6e6;border:2px solid #444"></div>
  <div class="partner" style="left:152px;width:64px"></div>
  <div class="partner round" style="left:238px"></div>
  <div class="partner" style="left:286px;width:50px;background:#555"></div>
  <div class="partner round" style="left:348px;background:#444"></div>
  <div class="partner" style="left:382px;width:40px;background:#ccc"></div>
  <div class="partner" style="left:446px;width:52px;background:#b7c2d8"></div>
  <div class="partner round" style="left:514px;background:#e6e6e6;border:2px solid #444"></div>
  <div class="partner" style="left:584px;width:64px"></div>
  <div class="partner round" style="left:670px"></div>
  <svg class="abs" style="left:712px;top:14px" width="8" height="12" viewBox="0 0 8 12"><path d="M2 1l5 5-5 5" fill="none" stroke="#222" stroke-width="2"/></svg>
</div>

<div class="ticker">
  <span class="up">▲</span>
  <span>GBP/UAH = <b class="up">12.65761 ▲</b></span>
  <span>GBP/UGX = <b class="down">4010.06174 ▼</b></span>
  <span>GBP/USD = <b class="up">1.55817 ▲</b></span>
  <span>GBP/UYU = <b class="up">34.36026 ▲</b></span>
  <span>GBP/VEF = <b class="flat">0</b></span>
  <span>GBP/VUV = <b class="up">151.3</b></span>
</div>

<footer class="site-footer">
  <div class="footer-col" style="left:60px">
    <h4>About Us</h4>
    <ul><li>History</li><li>Expertize</li><li>Identity</li><li>Strategy</li><li>Contact Us</li></ul>
  </div>
  <div class="footer-col" style="left:169px">
    <h4>Investements</h4>
    <ul><li>Term Deposits</li><li>Management &amp; Strategy</li><li>Client Relations</li><li>Financial Privacy</li><li>Tax Advice</li><li>Welth Analysis &amp; Financial Planning</li><li>Active Advisory Group</li><li>Manager Selection Services</li><li>Private Equity</li></ul>
  </div>
  <div class="footer-col" style="left:349px">
    <h4>Funds</h4>
    <ul><li>Overview</li><li>Administration</li><li>Funds Security</li><li>Core Services</li><li>Reporting</li><li>Revenue Opportunities</li><li>How it works?</li><li>Glossary</li></ul>
  </div>
  <div class="footer-col" style="left:484px">
    <h4>Currency Exchange</h4>
    <ul><li>Foreign Exchange</li><li>Fx Forward</li><li>Fx Options</li></ul>
    <h4 style="margin-top:16px">Accounts</h4>
    <ul><li>Apply Now</li><li>Private Access</li></ul>
  </div>
  <div class="footer-col" style="left:632px">
    <h4>Brokerage</h4>
    <ul><li>Institutional</li><li>Research</li><li>Trading</li></ul>
    <h4 style="margin-top:12px">Verified and Protected by</h4>
  </div>
  <div class="verified">
    <div class="abs" style="left:10px;top:10px;width:42px;height:20px;background:#b7c2d8"></div>
    <div class="abs" style="left:68px;top:6px;width:26px;height:26px;border-radius:50%;border:2px solid #444"></div>
    <div class="abs" style="left:10px;top:40px;width:48px;height:20px;background:#cfcfcf"></div>
    <div class="abs" style="left:68px;top:38px;width:26px;height:26px;border-radius:50%;background:#3a3a3a"></div>
  </div>
  <div class="copyright">© Copyright 2013 Marlowe Capital Group - All rights reserved.</div>
</footer>

</body>
</html>
```